Flyer Design Project

We would like a double sided a5 flyer. To promote our new brand which is velvetine mobile, attached is the logo. This is for a mobile telecom company.
The aim of the flyer is to create brand awareness, to pormote a managed service for mobile phone connections/ tariffs. For business users and also personal use.

We would like to focus to be on offshore billing and discrete billing for users based abroad. eg students

Theme should be based around Plumleaf and Zorphones , one side should focus on business users and the other should focus on personal use. The focus on business users should be based around , Virtual landline numbers, where users can have a landline number connected to their mobile phones.
Should be elegant, up class ,and not to much text bullet points would be good .

Branding of telecoms QX ,K7 ,Telmarix,.
Updates

Velvetine mobile

Contact info for the flyer. 
info@velvetinemobile.example
www.velvetinemobile.example
0871 463 19 19 

Flyers need to look elegant and good creative designs please.

Industry/Entity Type

Telecom

```html
<!DOCTYPE html>
<html lang="en">
<head>
<meta charset="utf-8">
<title>Velvetine mobile – flyer, both sides</title>
<link rel="stylesheet" href="https://fonts.googleapis.com/css2?family=Open+Sans:wght@400;600;700;800&display=swap">
<style>
  :root {
    --page-bg: #3a3a3a;
    --business-bg: #1f0b0d;
    --personal-bg: #141414;
    --ink: #ffffff;
    --accent-green: #8cc63f;
    --accent-blue: #29a8e0;
    --art-dark: #2a2a2a;
  }
  * { box-sizing: border-box; margin: 0; padding: 0; }
  html, body {
    width: 1200px; height: 1000px; overflow: hidden;
    background: var(--page-bg);
    font-family: "Open Sans", Arial, sans-serif;
    color: var(--ink);
  }
  .flyer {
    position: absolute;
    width: 700px; height: 460px;
    text-transform: uppercase;
    box-shadow: 0 8px 24px rgba(0,0,0,.5);
  }
  .flyer--business { left: 40px; top: 40px; background: var(--business-bg); }
  .flyer--personal { left: 470px; top: 490px; width: 680px; height: 470px; background: var(--personal-bg); }

  .brand {
    position: absolute; top: 22px; left: 0; right: 0;
    display: flex; flex-direction: column; align-items: center; gap: 6px;
  }
  .brand__mark { width: 14px; height: 14px; background: var(--ink); }
  .brand__name { font-size: 13px; font-weight: 400; letter-spacing: .5px; }

  /* Business side */
  .business__headline {
    position: absolute; top: 72px; left: 0; right: 0; text-align: center;
    font-size: 31px; font-weight: 400; letter-spacing: .5px;
  }
  .business__headline strong { font-weight: 700; }
  .business__frame {
    position: absolute; left: 34px; right: 34px; top: 122px; bottom: 62px;
    border: 3px solid var(--ink);
    display: flex; flex-direction: column; align-items: center; justify-content: center;
    text-align: center; line-height: 1.1;
  }
  .business__small { font-size: 14px; font-weight: 400; letter-spacing: .5px; }
  .business__mid { font-size: 26px; font-weight: 700; margin-bottom: 12px; }
  .business__big { font-size: 54px; font-weight: 800; line-height: 1; }

  .contact-bar {
    position: absolute; left: 0; right: 0; bottom: 20px; text-align: center;
    font-size: 11px; font-weight: 600; letter-spacing: .3px;
  }
  .contact-bar span + span::before { content: "|"; margin: 0 10px; }

  /* Personal side */
  .personal__headline {
    position: absolute; top: 96px; left: 0; right: 0; text-align: center;
    font-size: 40px; font-weight: 600; letter-spacing: 1px; line-height: 1.1;
  }
  .personal__sub { display: block; font-size: 21px; font-weight: 700; letter-spacing: .5px; }
  .personal__frame {
    position: absolute; left: 30px; right: 40px; top: 188px; bottom: 58px;
    border: 3px solid var(--ink);
    display: flex; align-items: center; padding: 0 24px;
  }
  .personal__copy { flex: 1; line-height: 1.1; }
  .personal__lead { font-size: 16px; font-weight: 400; margin-bottom: 4px; }
  .personal__offer { font-size: 33px; font-weight: 800; color: var(--accent-green); }
  .personal__tail { font-size: 16px; font-weight: 400; margin-top: 4px; }
  .personal__art {
    width: 190px; height: 190px;
    background: linear-gradient(160deg, #e8e8e8 0%, #6d8f45 55%, var(--accent-green) 100%);
    border-radius: 6px;
  }
</style>
</head>
<body>

<section class="flyer flyer--business" aria-label="Business side">
  <div class="brand"><span class="brand__mark"></span><span class="brand__name">Velvetine mobile</span></div>
  <h1 class="business__headline"><strong>Never miss</strong> a business <strong>call again!</strong></h1>
  <div class="business__frame">
    <p class="business__small">The complete telephone system solution for</p>
    <p class="business__mid">Small businesses</p>
    <p class="business__small">With an impressive range of</p>
    <p class="business__mid">Professional call handling features</p>
    <p class="business__small">Unilink Express allows small businesses to</p>
    <p class="business__big">Be responsive 24/7</p>
    <p class="business__small">By combining your landline and mobile calls</p>
  </div>
  <p class="contact-bar"><span>info@velvetinemobile.example</span><span>www.velvetinemobile.example</span><span>0871 463 19 19</span></p>
</section>

<section class="flyer flyer--personal" aria-label="Personal side">
  <div class="brand"><span class="brand__mark"></span><span class="brand__name">Velvetine mobile</span></div>
  <h2 class="personal__headline">Never miss a call again,<span class="personal__sub">Get your landline number on your mobile.</span></h2>
  <div class="personal__frame">
    <div class="personal__copy">
      <p class="personal__lead">Offshore and discrete billing</p>
      <p class="personal__offer">We will<br>save you money</p>
      <p class="personal__tail">Of your existing mobile provider.</p>
    </div>
    <div class="personal__art" role="img" aria-label="Illustration of three mobile phones showing dollar signs on their screens"></div>
  </div>
  <p class="contact-bar"><span>info@velvetinemobile.example</span><span>www.velvetinemobile.example</span><span>0871 463 19 19</span></p>
</section>

</body>
</html>
```